Bully breed rescue website

I need a website for my bully breed rescue. We rescue bully breeds from up and down the east coast of the United States and train them as service dogs for people with limited mobility disabilities. I don't want a lot of white space. I want it to be modern and slick and colorful and still look professional. I want it to be different and have a lot of wow factor. I linked a copy of my logo.

Number of Pages Required

5+ page

Font styles to use
Sans Serif

Colors

Designer to choose colors to be used in the design.

Requirements
Must have
• Moving aspects. Blog and ecommerce.
• 1.) Home page
• 2.) Services- something modular
• 3.) About US
• 4.) Blog
• 5.) Application page
• 6.) Donation page
• 7.) Contact Us
Nice to have
• Large Slider of photos on home page
• vertical menu bar
Should not have
• Lots of white space. Dont want it to look like a template or any other site

```html
<!DOCTYPE html>
<html lang="en">
<head>
<meta charset="utf-8">
<title>Steady Paws Rescue — Home</title>
<link rel="stylesheet" href="https://fonts.googleapis.com/css2?family=Open+Sans:wght@400;600;700&family=Barlow+Semi+Condensed:wght@400;500;600;700&display=swap">
<style>
  :root {
    --sidebar: #161818;
    --ink: #111111;
    --white: #ffffff;
    --mist: #d5d8de;
    --accent: #2ec98a;
    --panel: rgba(58, 58, 60, 0.78);
    --field: #f4f4f4;
    --black: #000000;
    --arrow: #777777;
  }
  * { box-sizing: border-box; margin: 0; padding: 0; }
  html, body { width: 1200px; height: 2250px; overflow: hidden; background: var(--black); }
  body { position: relative; font-family: "Open Sans", sans-serif; }

  /* Sidebar */
  .sidebar { position: absolute; left: 0; top: 0; width: 188px; height: 2250px; background: var(--sidebar); color: var(--white); }
  .sidebar-brand { position: absolute; top: 26px; left: 0; width: 188px; display: flex; flex-direction: column; align-items: center; gap: 6px; font-family: "Barlow Semi Condensed", sans-serif; font-weight: 700; font-size: 17px; white-space: nowrap; }
  .sidebar-brand .ring { width: 56px; height: 56px; border-radius: 50%; border: 2px solid var(--white); }
  .nav { position: absolute; top: 160px; left: 18px; width: 155px; list-style: none; }
  .nav li { height: 50px; display: flex; align-items: center; justify-content: space-between; font-size: 13px; font-weight: 600; }
  .nav li.active { height: 32px; border-bottom: 3px solid var(--white); margin-bottom: 14px; align-items: flex-start; }
  .nav svg { width: 18px; height: 18px; margin-right: 2px; }
  .search { position: absolute; top: 414px; left: 18px; width: 140px; height: 12px; background: var(--white); color: var(--ink); font-size: 7px; text-align: right; padding-right: 4px; line-height: 12px; }
  .social { display: flex; gap: 9px; }
  .social span { display: block; width: 20px; height: 20px; border: 2px solid var(--white); border-radius: 5px; }
  .sidebar .social { position: absolute; top: 448px; left: 51px; }

  /* Hero */
  .hero { position: absolute; left: 188px; top: 0; width: 1012px; height: 741px;
    background:
      radial-gradient(ellipse 28% 22% at 60% 55%, rgba(214,110,140,0.85) 0%, rgba(214,110,140,0) 100%),
      radial-gradient(ellipse 35% 30% at 45% 18%, rgba(176,98,62,0.9) 0%, rgba(176,98,62,0) 100%),
      radial-gradient(ellipse 40% 45% at 48% 45%, #eceae6 0%, rgba(220,212,204,0.9) 45%, rgba(220,212,204,0) 100%),
      radial-gradient(ellipse 30% 40% at 92% 15%, rgba(150,110,70,0.8) 0%, rgba(150,110,70,0) 100%),
      linear-gradient(110deg, #5f93b4 0%, #4d86ab 40%, #6e9cb8 75%, #8aa9bd 100%); }
  .band { position: absolute; left: 188px; top: 741px; width: 1012px; height: 77px; background: var(--mist); }
  .hero-brand { position: absolute; left: 848px; top: 30px; width: 307px; height: 230px; }
  .hero-brand .ring { position: absolute; left: 68px; top: 0; width: 170px; height: 170px; border-radius: 50%; border: 3px solid var(--ink); }
  .hero-brand .name { position: absolute; left: 0; top: 92px; width: 307px; text-align: center; white-space: nowrap; font-family: "Barlow Semi Condensed", sans-serif; font-weight: 700; font-size: 40px; line-height: 1; color: var(--ink); }

  .donate { position: absolute; left: 854px; top: 290px; width: 300px; height: 499px; background: var(--panel); color: var(--white); padding: 0 45px; }
  .donate h2 { font-weight: 400; font-size: 29px; text-align: center; margin-top: 27px; margin-bottom: 52px; }
  .donate label { display: block; font-size: 8px; font-weight: 600; height: 11px; }
  .donate .field { height: 33px; background: var(--field); border: 1px solid #ccc; border-radius: 2px; margin-bottom: 16px; }

  .btn { display: flex; align-items: center; justify-content: center; background: var(--accent); color: var(--white); border-radius: 5px; font-family: "Barlow Semi Condensed", sans-serif; font-weight: 500; font-size: 19px; letter-spacing: 0.5px; }
  .donate .btn { margin-top: 59px; height: 38px; font-family: "Open Sans", sans-serif; font-size: 17px; border-radius: 0; }

  /* Welcome */
  .welcome { position: absolute; left: 188px; top: 818px; width: 1012px; height: 340px; background: var(--white); }
  .welcome h1 { position: absolute; left: 79px; top: 52px; font-family: "Barlow Semi Condensed", sans-serif; font-weight: 600; font-size: 48px; letter-spacing: 3px; color: var(--ink); }
  .welcome p { position: absolute; left: 79px; top: 121px; width: 480px; font-family: "Barlow Semi Condensed", sans-serif; font-size: 16px; line-height: 1.55; color: var(--ink); }
  .welcome .btn { position: absolute; left: 79px; top: 240px; width: 154px; height: 49px; font-size: 23px; border-radius: 8px; }
  .welcome-photo { position: absolute; left: 589px; top: 0; width: 300px; height: 340px;
    background:
      radial-gradient(ellipse 18% 14% at 52% 38%, rgba(215,95,150,0.75) 0%, rgba(215,95,150,0) 100%),
      radial-gradient(ellipse 20% 18% at 30% 15%, rgba(170,95,70,0.7) 0%, rgba(170,95,70,0) 100%),
      radial-gradient(ellipse 45% 55% at 50% 55%, #f7eeee 0%, #eedada 60%, rgba(238,218,218,0) 100%),
      linear-gradient(180deg, #f6f4f4 0%, #f1ecec 100%); }

  /* Slider */
  .slider { position: absolute; left: 188px; top: 1158px; width: 1012px; height: 342px; background: var(--black); border-top: 2px solid #3a3a3a; border-bottom: 2px solid #3a3a3a; }
  .slide-photo { position: absolute; left: 408px; top: 0; width: 196px; height: 338px;
    background:
      radial-gradient(ellipse 40% 18% at 48% 20%, #b8b8b8 0%, rgba(184,184,184,0) 100%),
      radial-gradient(ellipse 45% 35% at 55% 62%, #d8d8d8 0%, #7a7a7a 50%, rgba(60,60,60,0) 100%),
      linear-gradient(90deg, #0a0a0a 0%, #202020 50%, #0a0a0a 100%); }
  .arrow { position: absolute; top: 144px; width: 52px; height: 52px; }
  .arrow.prev { left: 78px; }
  .arrow.next { left: 890px; }

  /* Gallery */
  .gallery { position: absolute; left: 188px; top: 1500px; width: 1012px; height: 408px; background: var(--mist); }
  .gallery-photo { position: absolute; }
  .gallery-photo.one { left: 150px; top: 54px; width: 190px; height: 290px;
    background:
      radial-gradient(ellipse 45% 25% at 60% 68%, #c07a3e 0%, rgba(192,122,62,0) 100%),
      linear-gradient(180deg, #7a5a40 0%, #a8846a 35%, #ece6dc 70%, #f2eee6 100%); }
  .gallery-photo.two { left: 399px; top: 54px; width: 240px; height: 225px;
    background:
      radial-gradient(ellipse 45% 30% at 45% 55%, #c48a58 0%, rgba(196,138,88,0) 100%),
      linear-gradient(180deg, #3f5a2a 0%, #5e7a36 45%, #9a8a46 75%, #b8a060 100%); }
  .gallery-photo.three { left: 697px; top: 50px; width: 209px; height: 294px;
    background:
      radial-gradient(ellipse 40% 35% at 48% 50%, #1a1a1a 0%, #252320 60%, rgba(37,35,32,0) 100%),
      linear-gradient(160deg, #6a6246 0%, #3a382c 50%, #4c5a34 100%); }
  .gallery .btn { position: absolute; left: 451px; top: 309px; width: 137px; height: 45px; font-size: 21px; }

  /* Contact */
  .contact { position: absolute; left: 188px; top: 1908px; width: 1012px; height: 342px; background: var(--black); color: var(--white); }
  .contact h2 { position: absolute; left: 0; top: 22px; width: 1012px; text-align: center; font-family: "Barlow Semi Condensed", sans-serif; font-weight: 600; font-size: 40px; letter-spacing: 1px; }
  .input-line { position: absolute; font-family: "Barlow Semi Condensed", sans-serif; font-weight: 700; font-size: 12px; letter-spacing: 0.5px; border-bottom: 3px solid var(--white); height: 18px; }
  .input-line.name { left: 272px; top: 84px; width: 135px; }
  .input-line.email { left: 451px; top: 84px; width: 135px; }
  .input-line.phone { left: 630px; top: 84px; width: 135px; }
  .input-line.message { left: 272px; top: 145px; width: 492px; }
  .contact .btn { position: absolute; left: 459px; top: 194px; width: 120px; height: 39px; font-size: 19px; }
  .contact .social { position: absolute; left: 463px; top: 260px; gap: 11px; }
  .contact .social span { width: 30px; height: 30px; border-width: 3px; border-radius: 8px; }
  .copyright { position: absolute; left: 0; top: 311px; width: 1012px; text-align: center; font-size: 7px; font-weight: 600; color: var(--white); }
</style>
</head>
<body>
  <aside class="sidebar">
    <div class="sidebar-brand"><span class="ring"></span>Steady Paws Rescue</div>
    <ul class="nav">
      <li class="active">Home</li>
      <li>Services <svg viewBox="0 0 18 18"><circle cx="9" cy="9" r="7.5" fill="none" stroke="#fff" stroke-width="1.2"/><path d="M8 5.5 11.5 9 8 12.5" fill="none" stroke="#fff" stroke-width="1.2"/></svg></li>
      <li>About Us <svg viewBox="0 0 18 18"><circle cx="9" cy="9" r="7.5" fill="none" stroke="#fff" stroke-width="1.2"/><path d="M8 5.5 11.5 9 8 12.5" fill="none" stroke="#fff" stroke-width="1.2"/></svg></li>
      <li>Blog <svg viewBox="0 0 18 18"><circle cx="9" cy="9" r="7.5" fill="none" stroke="#fff" stroke-width="1.2"/><path d="M8 5.5 11.5 9 8 12.5" fill="none" stroke="#fff" stroke-width="1.2"/></svg></li>
      <li>Contact Us <svg viewBox="0 0 18 18"><circle cx="9" cy="9" r="7.5" fill="none" stroke="#fff" stroke-width="1.2"/><path d="M8 5.5 11.5 9 8 12.5" fill="none" stroke="#fff" stroke-width="1.2"/></svg></li>
    </ul>
    <div class="search">Search</div>
    <div class="social"><span></span><span></span><span></span></div>
  </aside>

  <section class="hero" role="img" aria-label="Close-up photo of a smiling white and brown bulldog with its tongue out"></section>
  <div class="band"></div>
  <div class="hero-brand"><span class="ring"></span><span class="name">Steady Paws Rescue</span></div>

  <form class="donate">
    <h2>Donate Now</h2>
    <label>First Name</label><div class="field"></div>
    <label>Last Name</label><div class="field"></div>
    <label>Amount</label><div class="field"></div>
    <label>Email</label><div class="field"></div>
    <div class="btn">DONATE</div>
  </form>

  <section class="welcome">
    <h1>Welcome</h1>
    <p>We rescue bully breeds from up and down<br>the east coast of the United States and train them as service dogs for people,<br>with limited mobility disabilities.</p>
    <div class="btn">Learn more</div>
    <div class="welcome-photo" role="img" aria-label="Photo of a white bulldog puppy sitting"></div>
  </section>

  <section class="slider">
    <svg class="arrow prev" viewBox="0 0 52 52"><circle cx="26" cy="26" r="24" fill="none" stroke="#777" stroke-width="3"/><path d="M30 15 19 26 30 37" fill="none" stroke="#777" stroke-width="3"/></svg>
    <div class="slide-photo" role="img" aria-label="Black and white photo of a bulldog sitting in shadow"></div>
    <svg class="arrow next" viewBox="0 0 52 52"><circle cx="26" cy="26" r="24" fill="none" stroke="#777" stroke-width="3"/><path d="M22 15 33 26 22 37" fill="none" stroke="#777" stroke-width="3"/></svg>
  </section>

  <section class="gallery">
    <div class="gallery-photo one" role="img" aria-label="Photo of a bulldog puppy lying on a bed"></div>
    <div class="gallery-photo two" role="img" aria-label="Photo of a bulldog puppy walking on grass"></div>
    <div class="btn">Abous Us</div>
    <div class="gallery-photo three" role="img" aria-label="Photo of a black pug sitting indoors"></div>
  </section>

  <footer class="contact">
    <h2>Contacts Us</h2>
    <div class="input-line name">YOUR NAME</div>
    <div class="input-line email">EMAIL</div>
    <div class="input-line phone">PHONE</div>
    <div class="input-line message">MESSANGE</div>
    <div class="btn">Email</div>
    <div class="social"><span></span><span></span><span></span></div>
    <p class="copyright">Copyright 2018 - 2019. All Rights Reserved</p>
  </footer>
</body>
</html>
```